BRAYLEN AT HEARTH, LLC Webpage portfolio

I want to create a Website that allows my potential clients to browse my Skilled work via before and after photos. I want the website to enhance the work that I provide and potentially drive new business, or at least solidify my work.
I also do 3D CAD and Modeling of New Spaces and it would be nice to show some of that work from pencil design to 3D modeling, which I feel may help give me more clients.

The website needs to show a solid carpenter/company with the skills to get any project completed.

Types of Jobs - Custom Carpentry & Finishes, Kitchens, Baths, Basements, Decks, Porches, Whole House Renovation - Skilled Craftsmanship (Hardwood Flooring, Floor and Wall Tile) and much more...

Target Market(s)

Residential Home Renovation, Kitchen and Bath Renovation, Home Improvement

Industry/Entity Type

Residential Construction

Number of Pages Required

5+ page

Font styles to use
Sans Serif
Script

Requirements
Must have
• Similar to Nestlyra.com, except for Braylen At Hearth.
• Must be inviting.
• My Services Offered
• A way to reach me or contact me for estimates with some sort of Screening Questionare.
Nice to have
• Inviting Colors
Should not have
• Not sure at this time

```html
<!DOCTYPE html>
<html lang="en">
<head>
<meta charset="utf-8">
<title>Braylen At Hearth — Design, Build &amp; Remodeling</title>
<link rel="stylesheet" href="https://fonts.googleapis.com/css2?family=Questrial&family=Open+Sans:ital,wght@0,400;0,600;0,700;1,400&display=swap">
<style>
:root{
  --navy:#123e68;
  --navy-dark:#0c2c4c;
  --accent:#2aa1dc;
  --text:#6d6d6d;
  --text-dark:#3a3a3a;
  --panel:#f4f4f4;
  --rule:#e3e3e3;
  --footer:#363636;
  --footer-text:#b9b9b9;
  --white:#ffffff;
}
*{box-sizing:border-box;margin:0;padding:0}
html,body{width:1200px;height:3557px;overflow:hidden}
body{font-family:"Open Sans",Arial,sans-serif;color:var(--text);background:var(--white);position:relative}
.heading{font-family:"Questrial","Open Sans",sans-serif;font-weight:400;color:var(--navy);letter-spacing:2px;text-transform:uppercase}
section,header,footer{position:absolute;left:0;width:1200px}
.btn{display:inline-block;background:var(--accent);color:var(--white);font-size:13px;font-weight:600;letter-spacing:1px;text-transform:uppercase;text-align:center;line-height:48px;height:48px}
.fill{position:absolute}

/* Header */
.site-header{top:0;height:118px;background:var(--white)}
.brand{position:absolute;left:76px;top:26px;display:flex;flex-direction:column}
.brand-name{display:flex;align-items:center;gap:10px;font-family:"Questrial",sans-serif;font-size:27px;color:var(--navy);font-weight:400}
.brand-name .mark{width:22px;height:22px;background:var(--navy)}
.brand-tag{font-size:9px;letter-spacing:1px;color:var(--navy);text-transform:uppercase;margin-top:4px;padding-left:32px}
.topbar{position:absolute;right:76px;top:26px;display:flex;gap:26px;font-size:14px;color:var(--navy-dark)}
.topbar span{display:flex;align-items:center;gap:8px}
.main-nav{position:absolute;right:58px;top:78px;display:flex;gap:0}
.main-nav a{font-size:12.5px;color:var(--text-dark);text-decoration:none;text-transform:uppercase;letter-spacing:.5px;padding:0 19px 14px;position:relative}
.main-nav a.active{color:var(--accent)}
.main-nav a.active::after{content:"";position:absolute;left:10px;right:10px;bottom:0;height:2px;background:var(--accent)}

/* Hero */
.hero{top:118px;height:527px;background:linear-gradient(180deg,#3b2415 0%,#6b4226 35%,#5a3a24 65%,#2a1a10 100%)}
.hero-shade{position:absolute;inset:0;background:rgba(0,0,0,.22)}
.hero-content{position:absolute;top:190px;left:0;width:1200px;text-align:center;color:var(--white)}
.hero-title{font-family:"Questrial",sans-serif;font-size:72px;letter-spacing:3px;line-height:1}
.hero-sub{font-size:23px;line-height:30px;margin:18px auto 0;width:780px}
.hero .btn{width:164px;margin-top:28px}
.slide-arrow{position:absolute;top:237px}

/* What we do */
.services{top:645px;height:351px}
.section-title{position:absolute;left:0;width:1200px;text-align:center;font-size:30px}
.services .section-title{top:44px}
.service{position:absolute;top:115px;width:300px;text-align:center}
.service h3{font-size:14px;color:var(--accent);font-weight:400;text-transform:uppercase;letter-spacing:1px;margin-top:14px}
.service p{font-size:13.5px;line-height:24px;margin-top:6px}

/* About */
.about{top:996px;height:420px;background:var(--panel)}
.about-photo{left:0;top:0;width:600px;height:420px;background:linear-gradient(135deg,#5c3522 0%,#8a5a3a 40%,#3d2a22 75%,#1d1715 100%)}
.about-text{position:absolute;left:633px;top:42px;width:500px}
.about-text h2{font-size:32px}
.about-text p{font-size:13.5px;line-height:25px;margin-top:16px}
.about-text p + p{margin-top:10px}
.about-text .btn{width:162px;margin-top:18px}

/* Jobs */
.jobs{top:1416px;height:422px}
.jobs-panel{position:absolute;left:0;top:0;width:600px;height:422px;background:var(--panel)}
.jobs-panel h2{position:absolute;left:74px;top:48px;font-size:30px}
.job{position:absolute;width:170px;text-align:center;font-size:12px;color:var(--text-dark);line-height:17px}
.job svg{display:block;margin:0 auto 8px}
.dots{position:absolute;top:1798px;left:0}
.jobs-dots{position:absolute;left:304px;top:376px;display:flex;gap:6px}
.jobs-dots i{width:10px;height:10px;border-radius:50%;background:#9a9a9a}
.jobs-dots i.on{background:var(--accent)}
.jobs-photo{left:600px;top:0;width:600px;height:422px;background:linear-gradient(160deg,#7a6040 0%,#c9a675 45%,#a88458 70%,#5b4a36 100%)}

/* Before & After */
.before-after{top:1838px;height:503px}
.before-after .section-title{top:52px}
.ba-photo{top:116px;height:335px}
.ba-before{left:92px;width:503px;background:linear-gradient(135deg,#4c3a2a 0%,#8a6b48 40%,#6e5a46 70%,#3a2e26 100%)}
.ba-after{left:607px;width:501px;background:linear-gradient(135deg,#d8cdb8 0%,#a7865e 40%,#7e715f 70%,#3e3a36 100%)}
.ba-label{position:absolute;right:36px;bottom:22px;color:var(--white);font-size:15px;letter-spacing:1.5px}

/* Gallery */
.gallery{top:2341px;height:581px;background:var(--panel)}
.gallery .section-title{top:45px}
.g1{left:76px;top:97px;width:256px;height:206px;background:linear-gradient(135deg,#7a3a22,#3b2a24)}
.g2{left:344px;top:97px;width:332px;height:206px;background:linear-gradient(135deg,#d9d3c5,#8a6a48)}
.g3{left:690px;top:97px;width:437px;height:427px;background:linear-gradient(180deg,#cfdbe8 0%,#e8e2d6 40%,#8b6048 70%,#6b8a4a 100%)}
.g4{left:76px;top:319px;width:332px;height:205px;background:linear-gradient(135deg,#3a2a22,#9a8466 55%,#4a3a30)}
.g5{left:420px;top:319px;width:256px;height:205px;background:linear-gradient(180deg,#b9c9db 0%,#8a8c8e 40%,#6b6e70 80%,#5d7a3a 100%)}

/* Blog & Reviews */
.news{top:2922px;height:380px}
.news h2{position:absolute;top:50px;font-size:30px}
.pager{position:absolute;top:58px;display:flex;gap:10px}
.divider{position:absolute;left:600px;top:50px;width:1px;height:290px;background:var(--rule)}
.post{position:absolute;left:76px;width:500px;height:100px}
.post-thumb{left:0;top:0;width:152px;height:100px}
.post h3{position:absolute;left:178px;top:0;font-size:13.5px;color:var(--accent);font-weight:600;text-transform:uppercase;letter-spacing:.5px}
.post p{position:absolute;left:178px;top:24px;width:300px;font-size:13px;line-height:22px}
.post .more{position:absolute;left:178px;top:76px;font-size:11.5px;font-weight:700;color:var(--navy-dark);letter-spacing:.5px}
.review{position:absolute;left:631px;width:500px}
.review p{font-size:13px;line-height:22px;font-style:italic;padding-left:24px;position:relative}
.review p::before{content:"\201C";position:absolute;left:0;top:-6px;font-size:30px;font-style:normal;color:var(--accent);font-family:Georgia,serif}
.review .who{display:flex;align-items:center;gap:14px;margin-top:10px;padding-left:2px}
.avatar{width:48px;height:46px}
.review .name{font-size:11.5px;font-weight:700;color:var(--navy-dark);text-transform:uppercase}

/* Footer */
.site-footer{top:3302px;height:255px;background:var(--footer);color:var(--footer-text);font-size:12.5px}
.foot-brand{position:absolute;left:76px;top:42px}
.foot-brand .brand-name{color:#cfcfcf;font-size:24px}
.foot-brand .brand-name .mark{background:#cfcfcf;width:18px;height:18px}
.foot-brand .brand-tag{color:#9a9a9a;padding-left:28px}
.copyright{position:absolute;left:76px;top:136px;line-height:22px;font-size:12px}
.foot-col h4{position:absolute;font-size:12.5px;font-weight:400;color:var(--accent);text-transform:uppercase;letter-spacing:1px}
.foot-links{position:absolute;list-style:none;line-height:29px}
.contact-list{position:absolute;left:624px;top:76px;line-height:27px;list-style:none}
.contact-list strong{color:#e5e5e5}
.contact-list li{display:flex;align-items:center;gap:8px}
.foot-map{left:856px;top:50px;width:271px;height:154px;background:linear-gradient(135deg,#e9ecd8,#cfdcc6 50%,#e6e1d3)}
</style>
</head>
<body>

<header class="site-header">
  <div class="brand">
    <div class="brand-name"><span class="mark"></span>Braylen At Hearth</div>
    <div class="brand-tag">Design, build &amp; remodeling contractors</div>
  </div>
  <div class="topbar">
    <span><svg width="14" height="14" viewBox="0 0 24 24"><path fill="#123e68" d="M6.6 10.8a15 15 0 0 0 6.6 6.6l2.2-2.2c.3-.3.7-.4 1-.2 1.1.4 2.3.6 3.6.6.6 0 1 .4 1 1V20c0 .6-.4 1-1 1A17 17 0 0 1 3 4c0-.6.4-1 1-1h3.5c.6 0 1 .4 1 1 0 1.3.2 2.5.6 3.6.1.3 0 .7-.2 1z"/></svg>1-800-555-0148</span>
    <span><svg width="15" height="12" viewBox="0 0 24 18"><rect width="24" height="18" rx="2" fill="#123e68"/><path d="M2 3l10 7 10-7" stroke="#fff" stroke-width="2" fill="none"/></svg>hello@braylenathearth.com</span>
  </div>
  <nav class="main-nav">
    <a class="active">Home</a><a>About us</a><a>Services</a><a>Work Gallery</a><a>Blog</a><a>Clients</a><a>Reviews</a><a>Contact us</a>
  </nav>
</header>

<section class="hero">
  <div class="fill" style="inset:0" role="img" aria-label="Photo of a finished kitchen with wood cabinets and pendant lights"></div>
  <div class="hero-shade"></div>
  <svg class="slide-arrow" style="left:62px" width="30" height="54" viewBox="0 0 30 54"><path d="M26 4L4 27l22 23" stroke="#fff" stroke-opacity=".75" stroke-width="5" fill="none"/></svg>
  <svg class="slide-arrow" style="left:1106px" width="30" height="54" viewBox="0 0 30 54"><path d="M4 4l22 23L4 50" stroke="#fff" stroke-opacity=".75" stroke-width="5" fill="none"/></svg>
  <div class="hero-content">
    <h1 class="hero-title">Braylen At Hearth</h1>
    <p class="hero-sub">Consectetuer adipiscing elit, sed diam nonummy nibh euismod tincidunt ut laoreet dolore magna aliquam erat</p>
    <span class="btn">Read more</span>
  </div>
</section>

<section class="services">
  <h2 class="section-title heading">What we do</h2>
  <div class="service" style="left:90px">
    <svg width="72" height="72" viewBox="0 0 72 72"><g stroke="#2aa1dc" stroke-width="3" fill="none"><path d="M10 14l48 48M14 10l48 48M10 14l4-4"/><path d="M8 62L62 8l4 4L12 66z" fill="#2aa1dc" fill-opacity=".25"/><path d="M18 52l4 4M26 44l4 4M34 36l4 4M42 28l4 4M50 20l4 4"/></g></svg>
    <h3>Design</h3>
    <p>Vestibulum ante ipsum primis in faucibus orci luctus et ultrices posuere cubilia nibh a dui iaculis..</p>
  </div>
  <div class="service" style="left:450px">
    <svg width="72" height="72" viewBox="0 0 72 72"><g stroke="#2aa1dc" stroke-width="3" fill="#2aa1dc" fill-opacity=".25"><path d="M12 58l30-30 6 6-30 30z"/><path d="M38 14h16l6 8-8 4-6-4z"/><path d="M60 58L30 28"/><path d="M22 8a10 10 0 0 0 8 14l-4 4-12-12 4-4a10 10 0 0 0 4-2z"/><circle cx="62" cy="60" r="4"/></g></svg>
    <h3>Build</h3>
    <p>Vestibulum ante ipsum primis in faucibus orci luctus et ultrices posuere cubilia nibh a dui iaculis..</p>
  </div>
  <div class="service" style="left:806px">
    <svg width="72" height="72" viewBox="0 0 72 72"><g stroke="#2aa1dc" stroke-width="3" stroke-linejoin="round"><path d="M36 6l28 14v32L36 66 8 52V20z" fill="#2aa1dc" fill-opacity=".2"/><path d="M8 20l28 14 28-14M36 34v32" fill="none"/></g><text x="22" y="56" font-family="Open Sans,sans-serif" font-weight="700" font-size="18" fill="#2aa1dc">3D</text></svg>
    <h3>3D CAD &amp; Modeling</h3>
    <p>Vestibulum ante ipsum primis in faucibus orci luctus et ultrices posuere cubilia nibh a dui iaculis..</p>
  </div>
</section>

<section class="about">
  <div class="fill about-photo" role="img" aria-label="Photo of a living room with stone fireplace and built-in shelving"></div>
  <div class="about-text">
    <h2 class="heading">About Braylen At Hearth</h2>
    <p>Aliquam molestie, mi et imperdiet euismod, dui purus auctor tellus, et interdum lacus lectus et ante. Sed accumsan sollicitudin sapien, sit amet adipiscing turpis gravida ac. In congue, neque ac lobortis volutpat, libero mauris varius mi, vitae suscipit ipsum ligula vitae risus. Duis aliquam nibh a dui iaculis viverra id a velit.</p>
    <p>Vivamus egestas risus in magna varius commodo. Sed semper viverra egestas. Etiam pretium porttitor lectus, vel ornare neque porta volutpat.</p>
    <span class="btn">Read more</span>
  </div>
</section>

<section class="jobs">
  <div class="jobs-panel">
    <h2 class="heading">Job we offers</h2>
    <div class="job" style="left:67px;top:140px">
      <svg width="60" height="56" viewBox="0 0 60 56"><g stroke="#2aa1dc" stroke-width="2.2" fill="none"><circle cx="24" cy="12" r="7"/><path d="M12 52V34c0-8 6-12 12-12s12 4 12 12v18"/><path d="M36 30l14-14 4 4-14 14M6 52h48"/></g></svg>
      Custom Carpentry<br>&amp; Finishes</div>
    <div class="job" style="left:235px;top:140px">
      <svg width="64" height="56" viewBox="0 0 64 56"><g stroke="#2aa1dc" stroke-width="2.2" fill="none"><rect x="4" y="6" width="56" height="14"/><rect x="4" y="28" width="56" height="24"/><path d="M18 6v14M32 6v14M46 6v14M20 28v24M44 28v24M4 40h56"/></g></svg>
      Kitchens</div>
    <div class="job" style="left:401px;top:140px">
      <svg width="64" height="56" viewBox="0 0 64 56"><g stroke="#2aa1dc" stroke-width="2.2" fill="none"><path d="M6 28h52v8c0 8-6 12-12 12H18c-6 0-12-4-12-12z"/><path d="M14 28V10a6 6 0 0 1 12 0M16 48l-2 6M48 48l2 6"/></g></svg>
      Baths</div>
    <div class="job" style="left:67px;top:266px">
      <svg width="60" height="56" viewBox="0 0 60 56"><g stroke="#2aa1dc" stroke-width="2.2" fill="none"><path d="M16 20a14 14 0 0 1 28 0z"/><circle cx="30" cy="28" r="8"/><path d="M14 54V44c0-4 6-8 16-8s16 4 16 8v10M24 44h12"/></g></svg>
      Craftsmanship</div>
    <div class="job" style="left:235px;top:266px">
      <svg width="60" height="56" viewBox="0 0 60 56"><g stroke="#2aa1dc" stroke-width="2.2" fill="none"><path d="M8 4v48h44V4"/><path d="M20 4v14h20V4M14 30h32v22H14zM24 30v22M36 30v22"/></g></svg>
      Basements</div>
    <div class="job" style="left:401px;top:266px">
      <svg width="60" height="56" viewBox="0 0 60 56"><g stroke="#2aa1dc" stroke-width="2.2" fill="none"><path d="M4 28L30 4l26 24M12 22v30h36V22"/><path d="M24 52V36h12v16M40 10v8"/></g></svg>
      Whole House<br>Renovation</div>
    <div class="jobs-dots"><i class="on"></i><i></i></div>
  </div>
  <div class="fill jobs-photo" role="img" aria-label="Photo of an unfinished room with recessed lighting during renovation"></div>
</section>

<section class="before-after">
  <h2 class="section-title heading">Before &amp; After</h2>
  <svg class="fill" style="left:56px;top:272px" width="18" height="32" viewBox="0 0 18 32"><path d="M15 2L3 16l12 14" stroke="#9c9c9c" stroke-width="3" fill="none"/></svg>
  <svg class="fill" style="left:1126px;top:272px" width="18" height="32" viewBox="0 0 18 32"><path d="M3 2l12 14L3 30" stroke="#9c9c9c" stroke-width="3" fill="none"/></svg>
  <div class="fill ba-photo ba-before" role="img" aria-label="Before photo: stripped room with exposed framing"><span class="ba-label">BEFORE</span></div>
  <div class="fill ba-photo ba-after" role="img" aria-label="After photo: finished kitchen with white cabinets"><span class="ba-label">AFTER</span></div>
</section>

<section class="gallery">
  <h2 class="section-title heading">Work Gallery</h2>
  <div class="fill g1" role="img" aria-label="Photo of a kitchen island with wood cabinets"></div>
  <div class="fill g2" role="img" aria-label="Photo of a kitchen under renovation"></div>
  <div class="fill g3" role="img" aria-label="Photo of a covered porch with white railing and stone column"></div>
  <div class="fill g4" role="img" aria-label="Photo of a granite kitchen countertop"></div>
  <div class="fill g5" role="img" aria-label="Photo of a house exterior with new siding"></div>
</section>

<section class="news">
  <h2 class="heading" style="left:74px">Blog</h2>
  <div class="pager" style="left:502px"><svg width="8" height="14" viewBox="0 0 8 14"><path d="M7 1L1 7l6 6" stroke="#999" stroke-width="2" fill="none"/></svg><svg width="8" height="14" viewBox="0 0 8 14"><path d="M1 1l6 6-6 6" stroke="#333" stroke-width="2" fill="none"/></svg></div>
  <div class="post" style="top:98px">
    <div class="fill post-thumb" style="background:linear-gradient(135deg,#8b6a52,#d8d4cc 60%,#6a7a4a)" role="img" aria-label="Blog photo of a porch build"></div>
    <h3>Lorem ipsum dolor sit amet</h3>
    <p>Vestibulum ante ipsum primis in faucibus orci luctus et ultrices posuere cubilia nibh...</p>
    <span class="more">READ MORE</span>
  </div>
  <div class="post" style="top:235px">
    <div class="fill post-thumb" style="background:linear-gradient(135deg,#5a4a3a,#9aa8a8 55%,#3a3430)" role="img" aria-label="Blog photo of a kitchen remodel"></div>
    <h3>Lorem ipsum dolor sit amet</h3>
    <p>Vestibulum ante ipsum primis in faucibus orci luctus et ultrices posuere cubilia nibh...</p>
    <span class="more">READ MORE</span>
  </div>
  <div class="divider"></div>
  <h2 class="heading" style="left:631px">Client Reviews</h2>
  <div class="pager" style="left:1058px"><svg width="8" height="14" viewBox="0 0 8 14"><path d="M7 1L1 7l6 6" stroke="#999" stroke-width="2" fill="none"/></svg><svg width="8" height="14" viewBox="0 0 8 14"><path d="M1 1l6 6-6 6" stroke="#333" stroke-width="2" fill="none"/></svg></div>
  <div class="review" style="top:100px">
    <p>Vestibulum ante ipsum primis in faucibus orci luctus et ultrices posuere cubilia nibh eget turpis vehicula tempus ac sed massa...</p>
    <div class="who"><div class="avatar" style="background:#8a96a6" role="img" aria-label="Client portrait"></div><span class="name">- Name Heading</span></div>
  </div>
  <div class="review" style="top:234px">
    <p>Vestibulum ante ipsum primis in faucibus orci luctus et ultrices posuere cubilia nibh eget turpis vehicula tempus ac sed massa...</p>
    <div class="who"><div class="avatar" style="background:#d8b89a" role="img" aria-label="Client portrait"></div><span class="name">- Name Heading</span></div>
  </div>
</section>

<footer class="site-footer">
  <div class="foot-brand">
    <div class="brand-name"><span class="mark"></span>Braylen At Hearth</div>
    <div class="brand-tag">Design, build &amp; remodeling contractors</div>
  </div>
  <p class="copyright">Copyright © 2017, Braylen At Hearth<br>All Right Reserved</p>
  <div class="foot-col">
    <h4 style="left:353px;top:50px">Site map</h4>
    <ul class="foot-links" style="left:353px;top:80px"><li>Home</li><li>About us</li><li>Services</li><li>Work Gallery</li><li>Blog</li></ul>
    <ul class="foot-links" style="left:493px;top:80px"><li>Clients</li><li>Reviews</li><li>Contact us</li></ul>
    <h4 style="left:624px;top:50px">Contact info</h4>
  </div>
  <ul class="contact-list">
    <li style="display:block;line-height:20px"><strong>Braylen At Hearth</strong><br>4120 Alder Lane<br>Ashford, AF2 7KL</li>
    <li style="margin-top:6px"><svg width="12" height="12" viewBox="0 0 24 24"><path fill="#b9b9b9" d="M6.6 10.8a15 15 0 0 0 6.6 6.6l2.2-2.2c.3-.3.7-.4 1-.2 1.1.4 2.3.6 3.6.6.6 0 1 .4 1 1V20c0 .6-.4 1-1 1A17 17 0 0 1 3 4c0-.6.4-1 1-1h3.5c.6 0 1 .4 1 1 0 1.3.2 2.5.6 3.6.1.3 0 .7-.2 1z"/></svg>1-800-555-0148</li>
    <li><svg width="13" height="10" viewBox="0 0 24 18"><rect width="24" height="18" rx="2" fill="#b9b9b9"/><path d="M2 3l10 7 10-7" stroke="#363636" stroke-width="2" fill="none"/></svg>hello@braylenathearth.com</li>
  </ul>
  <div class="fill foot-map" role="img" aria-label="Street map showing the office location"></div>
</footer>

</body>
</html>
```